Flirt Wed or Ditch Show Flyer 2017

We are 3 female comedians who need to brand a new show that we want to take on the road. The show will be geared towards relationships. We will perform at clubs and theaters. We will also end up needing a logo etc for tee shirts and business cards and website. Etc. I am including some photos of the 3 of us from an old flyer from another show we did together ... it's not 'great' but it shows the 3 of us. ... perhaps there would be room for headshots also? or maybe we would add one shot of the 3 of us? There's also a chance we might want to include a 'guest' once in a while. The flyer should include space for the venue details and time date etc. and website. www.flirtwedorditch.example

Target Market(s)

Women. PG 13 and up. but not boxed in for just women. guys will have HUGE FUN TOO.

Logo Text

'Flirt Wed or Ditch'

Font styles to use
Sans Serif

Colors
e667a6
f04a50

Requirements
Must have
• Flirt Wed or Ditch
• possible tag lines- '3 comedians looking for love and finding the funny' or 'love means never having to say you're funny' or '3 funny women with choices'
• (we are still ironing out exactly the lines)
• names of 3 comedians: Nina Castell, Dorothy Vance, Tessa Wilbrook
• space to easily edit venue name - date - time
Should not have
• no swirly bits. it should look strong and powerful but feminine.

```html
<!DOCTYPE html>
<html lang="en">
<head>
<meta charset="utf-8">
<title>Flirt Wed or Ditch – Show Flyer</title>
<link rel="stylesheet" href="https://fonts.googleapis.com/css2?family=Bebas+Neue&family=Oswald:wght@500;600&display=swap">
<style>
  :root {
    --ink: #000000;
    --paper: #ffffff;
    --pink: #e667a6;
    --coral: #f04a50;
    --curtain-deep: #5a0608;
    --curtain: #b3121a;
    --curtain-bright: #d9242c;
    --heart: #e0141e;
    --photo-light: #d9b98f;
    --photo-dark: #3a2a2e;
  }
  html, body {
    margin: 0;
    padding: 0;
    background: var(--ink);
    overflow: hidden;
  }
  .flyer {
    position: relative;
    width: 800px;
    height: 1200px;
    background: var(--ink);
    overflow: hidden;
    color: var(--paper);
  }
  .stage {
    position: absolute;
    left: 0; top: 0;
    width: 800px; height: 530px;
    background:
      radial-gradient(ellipse at 50% 0%, rgba(255,255,255,0.18), transparent 55%),
      linear-gradient(180deg, var(--curtain-bright) 0%, var(--curtain) 45%, var(--curtain-deep) 85%, var(--ink) 100%);
  }
  .headshot {
    position: absolute;
    border-radius: 46% 46% 40% 40%;
  }
  .headshot--left {
    left: 64px; top: 168px; width: 216px; height: 296px;
    background: linear-gradient(180deg, var(--photo-light), #c79a72);
  }
  .headshot--center {
    left: 272px; top: 140px; width: 216px; height: 280px;
    background: linear-gradient(180deg, #e2c48c, #d6a889);
  }
  .headshot--right {
    left: 484px; top: 160px; width: 192px; height: 288px;
    background: linear-gradient(180deg, var(--photo-dark), #b98d80 45%, #2a2030);
  }
  .show-title {
    position: absolute;
    left: 0; top: 404px;
    width: 800px;
    margin: 0;
    text-align: center;
    font-family: "Bebas Neue", sans-serif;
    font-weight: 400;
    font-size: 110px;
    line-height: 1;
    letter-spacing: 3px;
    color: var(--paper);
  }
  .tagline {
    position: absolute;
    left: 0; top: 550px;
    width: 800px;
    margin: 0;
    text-align: center;
    font-family: "Bebas Neue", sans-serif;
    font-size: 41px;
    line-height: 1;
    color: var(--paper);
  }
  .featuring {
    position: absolute;
    left: 0; top: 608px;
    width: 800px;
    margin: 0;
    text-align: center;
    font-family: "Oswald", sans-serif;
    font-weight: 500;
    font-size: 17px;
    line-height: 24px;
    letter-spacing: 18px;
    text-indent: 18px;
    color: var(--pink);
  }
  .cast {
    position: absolute;
    left: 0; top: 652px;
    width: 800px;
    margin: 0; padding: 0;
    list-style: none;
    text-align: center;
  }
  .cast li {
    font-family: "Oswald", sans-serif;
    font-weight: 500;
    font-size: 56px;
    line-height: 64px;
    text-transform: uppercase;
    color: var(--paper);
  }
  .emblem {
    position: absolute;
    top: 645px;
    width: 136px; height: 220px;
    background: radial-gradient(ellipse at 50% 45%, var(--heart) 0%, #7a0a0f 45%, transparent 70%);
  }
  .emblem--left { left: 30px; }
  .emblem--right { left: 636px; }
  .promise {
    position: absolute;
    left: 127px; top: 884px;
    width: 541px; height: 58px;
    margin: 0;
    border: 2px solid var(--pink);
    box-sizing: border-box;
    display: flex;
    align-items: center;
    justify-content: center;
    font-family: "Bebas Neue", sans-serif;
    font-size: 32px;
    color: var(--paper);
  }
  .show-details {
    position: absolute;
    left: 0; top: 980px;
    width: 800px;
    text-align: center;
  }
  .venue {
    margin: 0;
    font-family: "Oswald", sans-serif;
    font-weight: 600;
    font-size: 34px;
    line-height: 44px;
    text-transform: uppercase;
    color: var(--pink);
  }
  .when {
    margin: 8px 0 0;
    font-family: "Bebas Neue", sans-serif;
    font-size: 30px;
    line-height: 34px;
    letter-spacing: 2px;
    color: var(--paper);
  }
  .website {
    margin: 22px 0 0;
    font-family: "Oswald", sans-serif;
    font-weight: 500;
    font-size: 22px;
    line-height: 28px;
    letter-spacing: 1px;
    color: var(--coral);
  }
  .footer-band {
    position: absolute;
    left: 0; top: 1176px;
    width: 800px; height: 24px;
    background: linear-gradient(90deg, var(--coral), var(--pink));
  }
</style>
</head>
<body>
  <main class="flyer">
    <div class="stage" role="img" aria-label="Red theatre curtains with stage spotlights on a lighting truss"></div>

    <div class="headshot headshot--left" role="img" aria-label="Headshot of a comedian with long blonde hair"></div>
    <div class="headshot headshot--center" role="img" aria-label="Headshot of a smiling comedian with blonde hair"></div>
    <div class="headshot headshot--right" role="img" aria-label="Headshot of a comedian with short dark hair"></div>

    <h1 class="show-title">Flirt Wed or Ditch</h1>

    <p class="tagline">Love means never having to say you're funny'</p>
    <p class="featuring">FEATURING COMEDIANS</p>

    <div class="emblem emblem--left" role="img" aria-label="Red heart pierced by a dagger"></div>
    <div class="emblem emblem--right" role="img" aria-label="Red heart pierced by a dagger"></div>

    <ul class="cast">
      <li>Tessa Wilbrook</li>
      <li>Dorothy Vance</li>
      <li>Nina Castell</li>
    </ul>

    <p class="promise">THIS SHOW WILL HAVE YOU IN STICHES...LITERALY</p>

    <section class="show-details">
      <p class="venue">Venue Name Here</p>
      <p class="when">Saturday, Month 00 &nbsp;·&nbsp; Doors 7PM &nbsp;·&nbsp; Show 8PM</p>
      <p class="website">www.flirtwedorditch.example</p>
    </section>

    <div class="footer-band"></div>
  </main>
</body>
</html>
```